Business Card for Orvane Parts Wholesale supplier

Hi There! I need a new business card for our company. We are specialized in selling Orvane parts, mostly we sell new LCD screens for Telvox and Slatrons. I would like to see that back in the design.

You can find the colors and logo's on our website: www.dorvak-example.nl

Industry/Entity Type

Business

Contact Information for Business Card

My Details:
Lars Vintorp

Phone: 0031612873406
E-mail: Lars@dorvak-example.nl

Slogan: "Because Quality Matters"

Font styles to use
Sans Serif

Colors

Designer to choose colors to be used in the design.

Requirements
Must have
• A Black backside with the Dorvak logo on it. The front side should be clean with only my contact details.
• But I'm also open for something really different or awesome!
Nice to have
• Remember that we are in the parts & repairing industry, So i'll be handing those business cards mainly to repair companies. Maybe you can do something with that thought :)

```html
<!DOCTYPE html>
<html lang="en">
<head>
<meta charset="utf-8">
<title>Dorvak business card</title>
<link href="https://fonts.googleapis.com/css2?family=Ubuntu:wght@400;500;700&display=swap" rel="stylesheet">
<style>
  :root {
    --page: #e4e4e2;
    --black: #141414;
    --black-soft: #262626;
    --grey-mark: #6e6e6e;
    --white: #ffffff;
    --paper-shade: #ececec;
    --orange: #f28a1e;
    --orange-deep: #d9700f;
    --ink: #1c1c1c;
    --rule: #3a3a3a;
  }
  * { margin: 0; padding: 0; box-sizing: border-box; }
  html, body {
    width: 1200px; height: 632px; overflow: hidden;
    background: var(--page);
    font-family: "Ubuntu", sans-serif;
  }
  .stage {
    position: relative; width: 1200px; height: 632px;
    display: flex; align-items: center; justify-content: center; gap: 60px;
  }
  .card {
    position: relative; width: 510px; height: 292px;
    border-radius: 3px; overflow: hidden;
    box-shadow: 0 10px 24px rgba(0,0,0,.18);
  }

  /* Back side */
  .card-back {
    background: radial-gradient(ellipse at 40% 30%, var(--black-soft), var(--black) 70%);
    border-bottom: 6px solid var(--orange);
  }
  .back-brand {
    position: absolute; left: 50%; top: 50%;
    transform: translate(-50%, -50%);
    display: flex; align-items: center; gap: 22px;
  }
  .back-brand .brand-square {
    width: 74px; height: 74px; background: var(--orange);
  }
  .back-brand .brand-name {
    font-size: 92px; font-weight: 500; color: var(--grey-mark);
    letter-spacing: -1px; line-height: 1;
  }

  /* Front side */
  .card-front {
    background: linear-gradient(180deg, var(--white), var(--paper-shade));
  }
  .front-brand {
    position: absolute; left: 250px; top: 34px;
    display: flex; align-items: center; gap: 10px;
  }
  .front-brand .brand-square { width: 24px; height: 24px; background: var(--orange); }
  .front-brand .brand-name { font-size: 30px; font-weight: 500; color: var(--ink); line-height: 1; }
  .top-rule {
    position: absolute; left: 250px; top: 82px; width: 218px; height: 1px; background: var(--rule);
  }
  .holder {
    position: absolute; left: 34px; top: 150px; width: 200px;
  }
  .holder-name {
    font-size: 17px; font-weight: 700; color: var(--orange);
    padding-bottom: 6px; border-bottom: 1px solid var(--rule);
  }
  .contact-list { list-style: none; margin-top: 12px; }
  .contact-list li {
    display: flex; align-items: center; gap: 7px;
    font-size: 11px; color: var(--ink); line-height: 17px;
  }
  .contact-list svg { width: 10px; height: 10px; fill: var(--orange); flex: none; }
  .slogan {
    position: absolute; right: 40px; top: 176px;
    font-size: 17px; color: var(--ink);
  }
  .slogan .accent { color: var(--orange); }
  .edge-band {
    position: absolute; left: 0; bottom: 0; width: 100%; height: 14px;
    background: var(--orange);
    border-top: 3px solid var(--orange-deep);
  }
</style>
</head>
<body>
<main class="stage">

  <section class="card card-back" aria-label="Card back">
    <div class="back-brand">
      <span class="brand-square"></span>
      <span class="brand-name">Dorvak</span>
    </div>
  </section>

  <section class="card card-front" aria-label="Card front">
    <div class="front-brand">
      <span class="brand-square"></span>
      <span class="brand-name">Dorvak</span>
    </div>
    <div class="top-rule"></div>

    <div class="holder">
      <p class="holder-name">Lars Vintorp</p>
      <ul class="contact-list">
        <li>
          <svg viewBox="0 0 24 24"><path d="M6.6 10.8c1.4 2.8 3.8 5.1 6.6 6.6l2.2-2.2c.3-.3.7-.4 1-.2 1.1.4 2.3.6 3.6.6.6 0 1 .4 1 1V20c0 .6-.4 1-1 1C10.6 21 3 13.4 3 4c0-.6.4-1 1-1h3.5c.6 0 1 .4 1 1 0 1.3.2 2.5.6 3.6.1.3 0 .7-.2 1z"/></svg>
          0031612873406
        </li>
        <li>
          <svg viewBox="0 0 24 24"><path d="M2 5h20v14H2z M4 7v1l8 5 8-5V7l-8 5z" fill-rule="evenodd"/></svg>
          Lars@dorvak-example.nl
        </li>
      </ul>
    </div>

    <p class="slogan">Because <span class="accent">Quality</span> Matters</p>

    <div class="edge-band"></div>
  </section>

</main>
</body>
</html>
```